Business Card Design Project

The business card is for an educational company that provides personalised tuition to students.

The company logo is in orange and blue (as provided) and should be included in the name card design

The philosophy of the company is to make learning a comfortable experience for student as such design of the namecard should look fresh and has a bit of the 'wow' factor. Some of the namecard design that appeals to me are as uploaded under Sample Design.

The particulars that need to be provided are:
(1): Company Name (Quillmark Education)
(1): Name
(2): Educational qualifications which will appear below name
(3): Mobile number
(4): Email address
(5): Website

Industry/Entity Type

Business

Requirements
Must have
• (1): Company Logo

(2): The card background should preferably be coloured both for the front side and back.

(3): The choice of font is important as part of the selection consideration. There is no preferred font that I have selected, designer is free to choose the font that will complement their design.

```html
<!DOCTYPE html>
<html lang="en">
<head>
<meta charset="utf-8">
<title>Quillmark Education — Business Card</title>
<link rel="stylesheet" href="https://fonts.googleapis.com/css2?family=Marcellus&display=swap">
<style>
  :root {
    --page-bg: #e9e9e7;
    --card-back: #0b0b0c;
    --card-front: #3a9bd9;
    --brand-grey: #4b4b4d;
    --back-grey: #6d6d70;
    --mark-orange: #ef7a1e;
    --ink-white: #ffffff;
  }
  * { box-sizing: border-box; margin: 0; padding: 0; }
  html, body { width: 1200px; height: 900px; overflow: hidden; }
  body {
    background: var(--page-bg);
    font-family: "Marcellus", serif;
    position: relative;
  }
  .card {
    position: absolute;
    left: 250px;
    width: 700px;
    height: 400px;
    border-radius: 3px;
    box-shadow: 0 6px 18px rgba(0,0,0,0.18);
  }
  .card--back { top: 30px; background: var(--card-back); }
  .card--front { top: 470px; background: var(--card-front); }

  .brand { position: absolute; display: flex; align-items: center; }
  .brand__square { flex: none; background: var(--mark-orange); border-radius: 6px; }
  .brand__name { line-height: 0.95; }

  .card--back .brand { left: 170px; top: 120px; gap: 22px; }
  .card--back .brand__square { width: 100px; height: 100px; }
  .card--back .brand__name { color: var(--back-grey); font-size: 52px; }
  .card--back .back-web {
    position: absolute; left: 170px; bottom: 48px;
    color: var(--back-grey); font-size: 19px; letter-spacing: 0.5px;
  }

  .holder { position: absolute; left: 88px; top: 72px; color: var(--ink-white); }
  .holder__name { font-size: 30px; letter-spacing: 1px; }
  .holder__title { font-size: 17px; margin-left: 14px; margin-top: 2px; }

  .card--front .brand { left: 340px; top: 50px; gap: 16px; }
  .card--front .brand__square { width: 72px; height: 72px; }
  .card--front .brand__name { color: var(--brand-grey); font-size: 36px; }

  .contact {
    position: absolute; left: 86px; top: 208px;
    list-style: none; color: var(--ink-white); font-size: 20px; line-height: 1.45;
  }
</style>
</head>
<body>
  <section class="card card--back" aria-label="Card back">
    <div class="brand">
      <div class="brand__square"></div>
      <div class="brand__name">Quillmark<br>Education</div>
    </div>
    <p class="back-web">www.quillmarkeducation.com</p>
  </section>

  <section class="card card--front" aria-label="Card front">
    <div class="holder">
      <p class="holder__name">JOHN DOE</p>
      <p class="holder__title">General manager</p>
    </div>
    <div class="brand">
      <div class="brand__square"></div>
      <div class="brand__name">Quillmark<br>Education</div>
    </div>
    <ul class="contact">
      <li>Phone: 555 210 4782</li>
      <li>Mobile: 55518293</li>
      <li>Email: info@quillmarkeducation.com</li>
      <li>Website: www.quillmarkeducation.com</li>
    </ul>
  </section>
</body>
</html>
```